Velvet Orchard Candle Company needs a Label design

We need a label design for a new candle company based in Charleston South Carolina. Our mission is to provide people with candles that will fill any space with fragrances that are uplifting, comforting, fresh and will make any space feel like home. Our candles are aromatherapy, 100% soy wax, and hand poured (we would love for this to be indicated somewhere on the label). We would like to see a label that is modern, very clean and uses pastel colors like green, blush pink, mauve and blush blue. The final design should communicate peace, gratitude, hope, and happiness.

```html
<!DOCTYPE html>
<html lang="en">
<head>
<meta charset="UTF-8">
<title>Honeysuckle Citrus Candle Label</title>
<link rel="stylesheet" href="https://fonts.googleapis.com/css2?family=Allura&family=Josefin+Sans:wght@300&family=Playfair+Display:wght@400;500&display=swap">
<style>
  :root {
    --page: #ffffff;
    --mint: #d3fcef;
    --ink: #ffffff;
  }
  html, body {
    margin: 0;
    padding: 0;
    overflow: hidden;
    background: var(--page);
  }
  .canvas {
    position: relative;
    width: 927px;
    height: 1200px;
    background: var(--page);
    overflow: hidden;
  }
  .label {
    position: absolute;
    left: 79px;
    top: 68px;
    width: 762px;
    height: 974px;
    background: var(--mint);
    border-radius: 74px;
  }
  .logo-mark {
    position: absolute;
    left: 0;
    top: 0;
    width: 927px;
    height: 320px;
  }
  .logo-arc {
    font-family: "Josefin Sans", sans-serif;
    font-weight: 300;
    font-size: 30px;
    font-variant: small-caps;
    letter-spacing: 2px;
    fill: var(--ink);
  }
  .logo-word {
    font-family: "Playfair Display", serif;
    font-weight: 500;
    font-size: 66px;
    fill: var(--ink);
  }
  .scent-name {
    position: absolute;
    left: 0;
    width: 927px;
    margin: 0;
    text-align: center;
    font-family: "Allura", cursive;
    font-weight: 400;
    color: var(--ink);
    line-height: 1;
  }
  .scent-name--first { top: 348px; font-size: 122px; }
  .scent-name--second { top: 500px; font-size: 122px; }
  .flourish {
    position: absolute;
    left: 248px;
    top: 673px;
    width: 410px;
    height: 128px;
    border-radius: 50%;
    background: radial-gradient(ellipse at center, rgba(255,255,255,0.55) 0%, rgba(255,255,255,0.25) 55%, rgba(255,255,255,0) 75%);
  }
  .features {
    position: absolute;
    left: 0;
    top: 881px;
    width: 927px;
    margin: 0;
    text-align: center;
    font-family: "Playfair Display", serif;
    font-weight: 400;
    font-size: 29px;
    font-variant: small-caps;
    letter-spacing: 0.2px;
    color: var(--ink);
    white-space: nowrap;
  }
</style>
</head>
<body>
  <div class="canvas">
    <div class="label"></div>

    <svg class="logo-mark" viewBox="0 0 927 320" aria-label="Logo placeholder">
      <defs>
        <path id="arc-top" d="M 393 195 A 70 70 0 0 1 533 195"/>
        <path id="arc-bottom" d="M 390 215 A 73 73 0 0 0 536 215"/>
      </defs>
      <text class="logo-arc"><textPath href="#arc-top" startOffset="50%" text-anchor="middle">Goes</textPath></text>
      <text class="logo-word" x="463" y="238" text-anchor="middle">LOGO</text>
      <text class="logo-arc"><textPath href="#arc-bottom" startOffset="50%" text-anchor="middle" dominant-baseline="hanging">Here</textPath></text>
    </svg>

    <h1 class="scent-name scent-name--first">Honeysuckle</h1>
    <p class="scent-name scent-name--second">Citrus</p>

    <div class="flourish" role="img" aria-label="Decorative white calligraphic flourish"></div>

    <p class="features">Aromatherapy - Hand Poured - 100% Soy Wax</p>
  </div>
</body>
</html>
```